Create Web Design Template with Source Files

I need a web design built with PSD/source files. See attached design I have made to guidance. Also I have attached an image I have used so you can use it.

I got my inspiration from this site if you would like to use it also:
http://trelvix.com/home

PSD & html slicing and responsive designs also. So we can run across all devices.

Number of Pages Required

1 page

Requirements
Must have
• See attachments. Ask if you have any questions...

```html
<!DOCTYPE html>
<html lang="en">
<head>
<meta charset="utf-8">
<title>VERVO — Where creators come first</title>
<link rel="stylesheet" href="https://fonts.googleapis.com/css2?family=Playfair+Display:wght@400;700&family=Roboto:wght@400;500;700&display=swap">
<style>
:root{
  --purple:#9c27b0;
  --teal:#26a9c4;
  --sidebar:#2c2b2d;
  --page:#f2f2f2;
  --ink:#222;
  --muted:#666;
  --footer:#dcdcdc;
  --white:#fff;
}
*{box-sizing:border-box;margin:0;padding:0}
html,body{width:1200px;height:2413px;overflow:hidden}
body{position:relative;background:var(--page);font-family:'Roboto',sans-serif;color:var(--ink)}
.abs{position:absolute}
.serif{font-family:'Playfair Display',serif}

.topbar{left:0;top:0;width:1200px;height:68px;background:var(--white);box-shadow:0 1px 3px rgba(0,0,0,.15);z-index:3}
.back-btn{left:18px;top:18px;width:32px;height:32px;border-radius:50%;background:var(--purple)}
.back-btn svg{position:absolute;left:9px;top:9px}
.brand{left:105px;top:17px;font-size:28px;font-weight:700;color:var(--purple);letter-spacing:.5px}
.search{left:1054px;top:26px}
.btn{display:flex;align-items:center;justify-content:center;gap:8px;color:var(--white);font-size:11px;border-radius:2px;box-shadow:0 2px 4px rgba(0,0,0,.25)}
.btn-purple{background:var(--purple)}
.btn-teal{background:var(--teal)}
.login{left:1099px;top:19px;width:82px;height:31px}

.sidebar{left:0;top:68px;width:286px;height:2345px;background:var(--sidebar)}
.sidebar-photo{left:0;top:0;width:286px;height:480px;background:linear-gradient(180deg,#4a4a4d 0%,#3d3c3f 55%,#2c2b2d 100%)}
.nav-item{left:18px;width:249px;height:36px;display:flex;align-items:center;padding-left:42px;color:#e8e8e8;font-size:12.5px}
.nav-item.active{background:var(--purple);color:var(--white);border-radius:2px}
.nav-item svg{position:absolute;left:13px;top:12px}

.hero{left:286px;top:68px;width:914px;height:374px;background:linear-gradient(180deg,#3b2a28 0%,#5a403a 45%,#2c2220 100%)}
.hero-title{left:286px;top:214px;width:914px;text-align:center;font-size:33px;color:var(--white)}
.hero-sub{left:286px;top:272px;width:914px;text-align:center;font-size:13px;color:var(--white)}

.slide-img{left:368px;top:463px;width:750px;height:359px;background:linear-gradient(180deg,#e9c98a 0%,#e8b87a 45%,#d99a66 70%,#b9876a 100%)}
.arrow{top:611px;width:36px;height:61px;background:var(--white);box-shadow:0 1px 4px rgba(0,0,0,.2)}
.arrow svg{position:absolute;left:12px;top:24px}
.slide-head{left:368px;top:845px;font-size:14.5px}
.slide-text{left:368px;top:876px;width:750px;font-size:10.5px;line-height:19px;color:#555}
.tags{left:368px;top:947px;display:flex;gap:26px;font-size:10px;color:var(--muted)}
.tags span::before{content:"";display:inline-block;width:4px;height:4px;border-radius:50%;background:#888;margin-right:8px;vertical-align:middle}
.tags .on{color:var(--purple)}
.tags .on::before{background:var(--purple)}
.opinion{left:368px;top:999px;width:100px;height:31px}

.sec-title{left:306px;font-size:20px;font-weight:700}
.sec-sub{left:306px;font-size:10px;color:#444}
.subscribe-top{left:1081px;top:1068px;width:100px;height:31px}

.thumb{width:204px;height:181px;background:linear-gradient(180deg,#ecd59c 0%,#e8bd82 50%,#c99670 100%)}
.avatar{width:22px;height:22px;border-radius:50%;background:#f1dede;border:2px solid #fff}
.dur{width:50px;height:22px;background:rgba(40,30,30,.8);color:#fff;font-size:10px;display:flex;align-items:center;justify-content:center}
.post-title{width:204px;font-size:12.5px;line-height:19px}
.post-meta{width:204px;display:flex;justify-content:space-between;font-size:9.5px;color:#444}
.load{width:100px;height:30px}

.channel{width:278px;height:184px;background:var(--white);box-shadow:0 1px 4px rgba(0,0,0,.18)}
.channel-img{left:0;top:0;width:278px;height:127px;background:linear-gradient(180deg,#ecd59c 0%,#e8bd82 55%,#c99670 100%)}
.channel-name{left:12px;top:139px;font-size:12px}
.channel-count{left:12px;top:162px;font-size:10px;color:#444}
.channel-sub{left:166px;top:139px;width:100px;height:31px}

.footer{left:286px;top:2365px;width:914px;height:48px;background:var(--footer);font-size:9.5px;color:#333}
.footer-links{left:155px;top:18px;display:flex;gap:22px;letter-spacing:.3px}
.copyright{left:562px;top:18px}
</style>
</head>
<body>

<header class="abs topbar">
  <div class="abs back-btn"><svg width="14" height="14" viewBox="0 0 14 14"><path d="M9 2 L4 7 L9 12" stroke="#fff" stroke-width="2" fill="none"/></svg></div>
  <div class="abs brand">VERVO</div>
  <svg class="abs search" width="16" height="16" viewBox="0 0 16 16"><circle cx="6.5" cy="6.5" r="4.5" stroke="#aaa" stroke-width="1.5" fill="none"/><path d="M10 10 L14 14" stroke="#aaa" stroke-width="1.5"/></svg>
  <div class="abs btn btn-purple login"><svg width="9" height="10" viewBox="0 0 9 10"><circle cx="4.5" cy="2.6" r="2.4" fill="#fff"/><path d="M0 10 C0 5.5 9 5.5 9 10Z" fill="#fff"/></svg>Login</div>
</header>

<aside class="abs sidebar">
  <div class="abs sidebar-photo" role="img" aria-label="Misty mountain landscape fading into the dark sidebar"></div>
  <nav>
    <div class="abs nav-item active" style="top:20px"><svg width="11" height="11" viewBox="0 0 11 11"><path d="M5.5 0 L11 5 H9.5 V11 H6.5 V7.5 H4.5 V11 H1.5 V5 H0Z" fill="#fff"/></svg>Home</div>
    <div class="abs nav-item" style="top:70px">How it works</div>
    <div class="abs nav-item" style="top:120px">About us</div>
    <div class="abs nav-item" style="top:170px">Weapons of comment</div>
  </nav>
</aside>

<section>
  <div class="abs hero" role="img" aria-label="Concert crowd cheering with raised arms, darkened"></div>
  <h1 class="abs hero-title serif" style="font-weight:400">Where creators come first</h1>
  <p class="abs hero-sub">Influence, Explore, and Create your world.</p>
</section>

<section>
  <div class="abs slide-img" role="img" aria-label="Four friends jumping on a beach at sunset"></div>
  <div class="abs arrow" style="left:306px"><svg width="10" height="12" viewBox="0 0 10 12"><path d="M7 1 L2 6 L7 11" stroke="#222" stroke-width="2" fill="none"/></svg></div>
  <div class="abs arrow" style="left:1143px"><svg width="10" height="12" viewBox="0 0 10 12"><path d="M3 1 L8 6 L3 11" stroke="#222" stroke-width="2" fill="none"/></svg></div>
  <h2 class="abs slide-head serif" style="font-weight:400">Lorem Ipsum is simply dummy text of the printing industry?</h2>
  <p class="abs slide-text">Lorem Ipsum is simply dummy text of the printing and typesetting industry. Lorem Ipsum has been the industry's standard dummy text ever since the 1500s, when an unknown printer took a galley of type and scrambled it to make a type specimen book. It has survived not only five centuries, but also the leap into electronic typesetting, remaining essentially unchanged.</p>
  <div class="abs tags"><span class="on">Lorem Ipsum</span><span>Lorem Ipsum text</span><span>Ipsum dummy text</span><span>Simply dumme text</span></div>
  <div class="abs btn btn-teal opinion">Your Opinion</div>
</section>

<section>
  <h2 class="abs sec-title serif" style="top:1062px">Lorem Ipsum is simply text</h2>
  <p class="abs sec-sub" style="top:1100px">Lorem Ipsum is simply dummy text</p>
  <div class="abs btn btn-purple subscribe-top"><svg width="7" height="10" viewBox="0 0 7 10"><path d="M0 0H7V10L3.5 7.5 0 10Z" fill="#fff"/></svg>Subscribe</div>

  <!-- row 1 -->
  <div class="abs thumb" style="left:306px;top:1136px" role="img" aria-label="Friends jumping on a beach at sunset"></div>
  <div class="abs thumb" style="left:529px;top:1136px" role="img" aria-label="Friends jumping on a beach at sunset"></div>
  <div class="abs thumb" style="left:753px;top:1136px" role="img" aria-label="Friends jumping on a beach at sunset"></div>
  <div class="abs thumb" style="left:976px;top:1136px" role="img" aria-label="Friends jumping on a beach at sunset"></div>
  <div class="abs avatar" style="left:319px;top:1147px" role="img" aria-label="Creator avatar"></div>
  <div class="abs avatar" style="left:542px;top:1147px" role="img" aria-label="Creator avatar"></div>
  <div class="abs avatar" style="left:766px;top:1147px" role="img" aria-label="Creator avatar"></div>
  <div class="abs avatar" style="left:989px;top:1147px" role="img" aria-label="Creator avatar"></div>
  <div class="abs dur" style="left:460px;top:1295px">2 min</div>
  <div class="abs dur" style="left:683px;top:1295px">2 min</div>
  <div class="abs dur" style="left:907px;top:1295px">2 min</div>
  <div class="abs dur" style="left:1130px;top:1295px">2 min</div>
  <p class="abs post-title serif" style="left:306px;top:1330px">Lorem Ipsum is simply dummy text of the printing and type industry.</p>
  <p class="abs post-title serif" style="left:529px;top:1330px">Lorem Ipsum is simply dummy text of the printing and type industry.</p>
  <p class="abs post-title serif" style="left:753px;top:1330px">Lorem Ipsum is simply dummy text of the printing and type industry.</p>
  <p class="abs post-title serif" style="left:976px;top:1330px">Lorem Ipsum is simply dummy text of the printing and type industry.</p>
  <div class="abs post-meta" style="left:306px;top:1382px"><span>Lorem Ipsum text</span><span>2 days ago</span></div>
  <div class="abs post-meta" style="left:529px;top:1382px"><span>Lorem Ipsum text</span><span>2 days ago</span></div>
  <div class="abs post-meta" style="left:753px;top:1382px"><span>Lorem Ipsum text</span><span>2 days ago</span></div>
  <div class="abs post-meta" style="left:976px;top:1382px"><span>Lorem Ipsum text</span><span>2 days ago</span></div>

  <!-- row 2 -->
  <div class="abs thumb" style="left:306px;top:1432px" role="img" aria-label="Friends jumping on a beach at sunset"></div>
  <div class="abs thumb" style="left:529px;top:1432px" role="img" aria-label="Friends jumping on a beach at sunset"></div>
  <div class="abs thumb" style="left:753px;top:1432px" role="img" aria-label="Friends jumping on a beach at sunset"></div>
  <div class="abs thumb" style="left:976px;top:1432px" role="img" aria-label="Friends jumping on a beach at sunset"></div>
  <div class="abs avatar" style="left:319px;top:1443px" role="img" aria-label="Creator avatar"></div>
  <div class="abs avatar" style="left:542px;top:1443px" role="img" aria-label="Creator avatar"></div>
  <div class="abs avatar" style="left:766px;top:1443px" role="img" aria-label="Creator avatar"></div>
  <div class="abs avatar" style="left:989px;top:1443px" role="img" aria-label="Creator avatar"></div>
  <div class="abs dur" style="left:460px;top:1591px">2 min</div>
  <div class="abs dur" style="left:683px;top:1591px">2 min</div>
  <div class="abs dur" style="left:907px;top:1591px">2 min</div>
  <div class="abs dur" style="left:1130px;top:1591px">2 min</div>
  <p class="abs post-title serif" style="left:306px;top:1626px">Lorem Ipsum is simply dummy text of the printing and type industry.</p>
  <p class="abs post-title serif" style="left:529px;top:1626px">Lorem Ipsum is simply dummy text of the printing and type industry.</p>
  <p class="abs post-title serif" style="left:753px;top:1626px">Lorem Ipsum is simply dummy text of the printing and type industry.</p>
  <p class="abs post-title serif" style="left:976px;top:1626px">Lorem Ipsum is simply dummy text of the printing and type industry.</p>
  <div class="abs post-meta" style="left:306px;top:1678px"><span>Lorem Ipsum text</span><span>2 days ago</span></div>
  <div class="abs post-meta" style="left:529px;top:1678px"><span>Lorem Ipsum text</span><span>2 days ago</span></div>
  <div class="abs post-meta" style="left:753px;top:1678px"><span>Lorem Ipsum text</span><span>2 days ago</span></div>
  <div class="abs post-meta" style="left:976px;top:1678px"><span>Lorem Ipsum text</span><span>2 days ago</span></div>

  <div class="abs btn btn-teal load" style="left:693px;top:1728px">Load More</div>
</section>

<section>
  <h2 class="abs sec-title serif" style="top:1790px">Lorem Ipsum is simply text</h2>
  <p class="abs sec-sub" style="top:1829px">Lorem Ipsum is simply dummy text</p>

  <div class="abs channel" style="left:306px;top:1864px"><div class="abs channel-img" role="img" aria-label="Friends jumping on a beach at sunset"></div><div class="abs channel-name serif">Lorem Ipsum text</div><div class="abs channel-count">10218 Videos</div><div class="abs btn btn-purple channel-sub"><svg width="7" height="10" viewBox="0 0 7 10"><path d="M0 0H7V10L3.5 7.5 0 10Z" fill="#fff"/></svg>Subscribe</div></div>
  <div class="abs channel" style="left:604px;top:1864px"><div class="abs channel-img" role="img" aria-label="Friends jumping on a beach at sunset"></div><div class="abs channel-name serif">Lorem Ipsum text</div><div class="abs channel-count">10218 Videos</div><div class="abs btn btn-purple channel-sub"><svg width="7" height="10" viewBox="0 0 7 10"><path d="M0 0H7V10L3.5 7.5 0 10Z" fill="#fff"/></svg>Subscribe</div></div>
  <div class="abs channel" style="left:903px;top:1864px"><div class="abs channel-img" role="img" aria-label="Friends jumping on a beach at sunset"></div><div class="abs channel-name serif">Lorem Ipsum text</div><div class="abs channel-count">10218 Videos</div><div class="abs btn btn-purple channel-sub"><svg width="7" height="10" viewBox="0 0 7 10"><path d="M0 0H7V10L3.5 7.5 0 10Z" fill="#fff"/></svg>Subscribe</div></div>

  <div class="abs channel" style="left:306px;top:2068px"><div class="abs channel-img" role="img" aria-label="Friends jumping on a beach at sunset"></div><div class="abs channel-name serif">Lorem Ipsum text</div><div class="abs channel-count">10218 Videos</div><div class="abs btn btn-purple channel-sub"><svg width="7" height="10" viewBox="0 0 7 10"><path d="M0 0H7V10L3.5 7.5 0 10Z" fill="#fff"/></svg>Subscribe</div></div>
  <div class="abs channel" style="left:604px;top:2068px"><div class="abs channel-img" role="img" aria-label="Friends jumping on a beach at sunset"></div><div class="abs channel-name serif">Lorem Ipsum text</div><div class="abs channel-count">10218 Videos</div><div class="abs btn btn-purple channel-sub"><svg width="7" height="10" viewBox="0 0 7 10"><path d="M0 0H7V10L3.5 7.5 0 10Z" fill="#fff"/></svg>Subscribe</div></div>
  <div class="abs channel" style="left:903px;top:2068px"><div class="abs channel-img" role="img" aria-label="Friends jumping on a beach at sunset"></div><div class="abs channel-name serif">Lorem Ipsum text</div><div class="abs channel-count">10218 Videos</div><div class="abs btn btn-purple channel-sub"><svg width="7" height="10" viewBox="0 0 7 10"><path d="M0 0H7V10L3.5 7.5 0 10Z" fill="#fff"/></svg>Subscribe</div></div>

  <div class="abs btn btn-teal load" style="left:693px;top:2291px">Load More</div>
</section>

<footer class="abs footer">
  <div class="abs footer-links"><span>TERMS OF SERVICE</span><span>PRIVACY</span><span>COPYRIGHT</span></div>
  <div class="abs copyright">Copyright © 2018 VERVO. All Rights Reserved.</div>
</footer>

</body>
</html>
```